Spectacular Business Card Design for AI SAAS Plattform called Leapvine.ai

Hi Creators
I need an outstanding new Design for my business card.
I run an AI automated Saas Plattform Called Leapvine.ai

Front side:
Logo
Slogan: DIY Business Development & Social Media Management
Data:
Name: Markus Obelwinter - CEO / Founder
email: m.obelwinter@leapvine.ai
mobile: +43 699 82 37 415

Company name:
Leapvine FlexCo

Backside:

What we stand for Slogan:
Vertrauen in KI-Technologie, getragen von menschlicher Vision: Dein Sprung nach vorn!
+ a fancy design what captures our core competencies - AI automisations, Social Media Management, Business development
(dont know if its too much, but AI and social media should be )

pls find attached the logo and the old design

Industry/Entity Type

AI automations for marketing and business development

Contact Information for Business Card

Front side: Logo Slogan: DIY Business Development & Social Media Management Data: Name: Markus Obelwinter - CEO / Founder email: m.obelwinter@leapvine.ai mobile: +43 699 82 37 415 Company name: Leapvine FlexCo Backside: What we stand for Slogan: Vertrauen in KI-Technologie, getragen von menschlicher Vision: Dein Sprung nach vorn!

Font styles to use
Serif
Sans Serif

Requirements
Nice to have
• a fancy design on the backside, a fancy design what captures our core competencies - AI automisations, Social Media Management, Business development

```html
<!DOCTYPE html>
<html lang="de">
<head>
<meta charset="utf-8">
<title>Leapvine – Business Card</title>
<link rel="stylesheet" href="https://fonts.googleapis.com/css2?family=Roboto:wght@400;500;700&display=swap">
<style>
  :root {
    --stage: #1c1d1f;
    --card-dark: #2a2a2b;
    --card-light: #ffffff;
    --teal: #0b8fae;
    --teal-deep: #07628a;
    --blue-edge: #0a7fa8;
    --orange: #f39a2f;
    --grey: #5d5f63;
    --white: #ffffff;
  }
  * { box-sizing: border-box; margin: 0; padding: 0; }
  html, body {
    width: 1200px; height: 840px; overflow: hidden;
    background: var(--stage);
    font-family: "Roboto", Arial, sans-serif;
  }
  .stage {
    position: relative; width: 1200px; height: 840px;
  }
  .card {
    position: absolute; left: 280px;
    width: 640px; height: 366px;
    border-radius: 26px; overflow: hidden;
  }

  /* Back side */
  .card--back {
    top: 40px;
    background: var(--card-dark);
    box-shadow: 0 5px 0 var(--blue-edge);
    display: flex; flex-direction: column; align-items: center; justify-content: center;
    text-align: center; color: var(--white);
  }
  .brand {
    display: flex; align-items: center; gap: 14px;
    font-weight: 500; color: var(--teal); letter-spacing: 0.5px;
  }
  .brand__mark { width: 18px; height: 18px; background: var(--orange); }
  .card--back .brand { font-size: 64px; margin-bottom: 26px; }
  .card--back .brand__mark { width: 22px; height: 22px; }
  .values { font-size: 17px; line-height: 1.45; }
  .values p + p { margin-top: 10px; }

  /* Front side */
  .card--front {
    top: 434px;
    background: var(--card-light);
    box-shadow: 0 5px 0 var(--blue-edge);
  }
  .card--front .brand {
    position: absolute; left: 42px; top: 92px; font-size: 62px;
  }
  .person {
    position: absolute; right: 42px; top: 34px; text-align: right;
  }
  .person__name {
    font-size: 24px; font-weight: 700; text-transform: uppercase; letter-spacing: 0.3px;
  }
  .person__first { color: var(--teal); }
  .person__last { color: var(--orange); }
  .person__role { font-size: 18px; color: var(--grey); margin-top: 4px; }

  .band {
    position: absolute; inset: 0;
    background: linear-gradient(100deg, var(--teal-deep) 0%, var(--teal) 45%, var(--teal) 100%);
    clip-path: polygon(0 66%, 55% 42%, 100% 36%, 100% 100%, 0 100%);
  }
  .contact {
    position: absolute; left: 46px; bottom: 30px; color: var(--white);
  }
  .contact__row {
    display: flex; align-items: center; gap: 10px; font-size: 19px; line-height: 1.4;
  }
  .contact__icon { width: 18px; height: 18px; flex: none; }
  .tagline { margin-top: 14px; font-size: 20px; line-height: 1.3; font-weight: 500; }
</style>
</head>
<body>
<main class="stage">

  <section class="card card--back" aria-label="Rückseite">
    <div class="brand"><span class="brand__mark"></span>Leapvine</div>
    <div class="values">
      <p>Vertrauen in KI-Technologie, getragen von menschlicher Vision:<br>Dein Sprung nach vorn!</p>
      <p>+ a fancy design what captures our core competencies -<br>AI automisations, Social Media Management, Business development</p>
    </div>
  </section>

  <section class="card card--front" aria-label="Vorderseite">
    <div class="band"></div>
    <div class="brand"><span class="brand__mark"></span>Leapvine</div>
    <div class="person">
      <div class="person__name"><span class="person__first">Markus</span> <span class="person__last">Obelwinter</span></div>
      <div class="person__role">CEO / Founder</div>
    </div>
    <div class="contact">
      <div class="contact__row">
        <svg class="contact__icon" viewBox="0 0 24 24" aria-hidden="true"><path fill="#fff" d="M6.6 10.8a15.1 15.1 0 0 0 6.6 6.6l2.2-2.2c.3-.3.7-.4 1-.2 1.1.4 2.3.6 3.6.6.6 0 1 .4 1 1V20c0 .6-.4 1-1 1A17 17 0 0 1 3 4c0-.6.4-1 1-1h3.5c.6 0 1 .4 1 1 0 1.3.2 2.5.6 3.6.1.3 0 .7-.2 1z"/></svg>
        <span>+43 699 82 37 415</span>
      </div>
      <div class="contact__row">
        <svg class="contact__icon" viewBox="0 0 24 24" aria-hidden="true"><path fill="#fff" d="M3 5h18c.6 0 1 .4 1 1v12c0 .6-.4 1-1 1H3c-.6 0-1-.4-1-1V6c0-.6.4-1 1-1zm9 7.5L4.5 7v1.8L12 14l7.5-5.2V7z"/></svg>
        <span>m.obelwinter@leapvine.ai</span>
      </div>
      <p class="tagline">DIY Business Development<br>&amp; Social Media Management</p>
    </div>
  </section>

</main>
</body>
</html>
```